diesel mechainc buisness card design

I need a business card for new company in congers ny called harbinger mobile rig & machinery repair I do onsite work ,engine repair, engine diagnosing , hydraulic system repair, welding and fabrication, servicing and preventive maintenance ,

Industry/Entity Type

Welding

Contact Information for Business Card

harbinger mobile rig & machinery repair ,dale morrow jr, congers ny 10920 phone number 8455730264 cell 8455604317 email dmrj47@mailvera.net

```html
<!DOCTYPE html>
<html lang="en">
<head>
<meta charset="utf-8">
<title>Harbinger Mobile Rig &amp; Machinery Repair — Business Card</title>
<link rel="stylesheet" href="https://fonts.googleapis.com/css2?family=Open+Sans:wght@400;600&family=Orbitron:wght@500&display=swap">
<style>
  :root {
    --backdrop: #e9e9ea;
    --card: #fafafa;
    --ink: #1f1f1f;
    --band: #232324;
    --accent: #1aaee6;
    --muted: #2c2c2c;
  }
  html, body {
    margin: 0;
    width: 1200px;
    height: 939px;
    overflow: hidden;
    background: var(--backdrop);
  }
  .canvas {
    position: relative;
    width: 1200px;
    height: 939px;
  }
  .card {
    position: absolute;
    left: 100px;
    top: 184px;
    width: 1000px;
    height: 571px;
    background: radial-gradient(ellipse at 60% 40%, #ffffff 0%, var(--card) 60%, #efefef 100%);
    box-shadow: 0 14px 40px rgba(0,0,0,.22);
    overflow: hidden;
    font-family: "Open Sans", Arial, sans-serif;
    color: var(--ink);
  }
  .band { position: absolute; left: 0; width: 100%; height: 32px; background: var(--band); }
  .band--top { top: 0; }
  .band--bottom { bottom: 0; }
  .tab {
    position: absolute;
    height: 40px;
    background: var(--accent);
    border: 3px solid var(--band);
    box-sizing: border-box;
  }
  .tab--top { top: 0; left: 54px; width: 284px; border-radius: 0 0 8px 8px; }
  .tab--bottom { bottom: 0; left: 160px; width: 290px; border-radius: 8px 8px 0 0; }
  .pointer { position: absolute; left: 0; top: 104px; width: 48px; height: 48px; }
  .person { position: absolute; left: 90px; top: 68px; }
  .person__name { margin: 0; font-size: 46px; font-weight: 400; letter-spacing: 0.5px; line-height: 1.1; }
  .person__role { margin: 6px 0 0 4px; font-size: 17px; }
  .contacts { position: absolute; left: 100px; top: 232px; }
  .contact { display: flex; align-items: center; gap: 14px; margin-bottom: 22px; font-size: 21px; line-height: 1.25; color: var(--muted); }
  .contact svg { width: 30px; height: 30px; flex: none; fill: var(--ink); }
  .company {
    position: absolute;
    right: 38px;
    top: 298px;
    margin: 0;
    text-align: right;
    font-family: "Orbitron", "Arial Narrow", sans-serif;
    font-weight: 500;
    font-size: 34px;
    line-height: 1.6;
    letter-spacing: 2px;
    color: var(--accent);
  }
</style>
</head>
<body>
<main class="canvas">
  <section class="card" aria-label="Business card">
    <div class="band band--top"></div>
    <div class="tab tab--top"></div>
    <div class="band band--bottom"></div>
    <div class="tab tab--bottom"></div>

    <svg class="pointer" viewBox="0 0 48 48" aria-hidden="true">
      <polygon points="0,4 32,4 46,24 32,44 0,44" fill="var(--accent)"/>
    </svg>

    <header class="person">
      <h1 class="person__name">JOHN DOE</h1>
      <p class="person__role">Managing Director</p>
    </header>

    <div class="contacts">
      <div class="contact">
        <svg viewBox="0 0 24 24" aria-hidden="true"><path d="M12 3 2 12h3v9h5v-6h4v6h5v-9h3z"/></svg>
        <span>14 Lakeview Rd<br>Congers NY 10920</span>
      </div>
      <div class="contact">
        <svg viewBox="0 0 24 24" aria-hidden="true"><path d="M12 2a10 10 0 1 0 0 20 10 10 0 0 0 0-20zm7.9 9h-3.4a15 15 0 0 0-1.3-6.2A8 8 0 0 1 19.9 11zM12 4.1c1 1.3 2.3 3.8 2.5 6.9h-5C9.7 7.9 11 5.4 12 4.1zM8.8 4.8A15 15 0 0 0 7.5 11H4.1a8 8 0 0 1 4.7-6.2zM4.1 13h3.4a15 15 0 0 0 1.3 6.2A8 8 0 0 1 4.1 13zM12 19.9c-1-1.3-2.3-3.8-2.5-6.9h5c-.2 3.1-1.5 5.6-2.5 6.9zm3.2-.7a15 15 0 0 0 1.3-6.2h3.4a8 8 0 0 1-4.7 6.2z"/></svg>
        <span>johndoe@mailvera.net<br>harbingerrigs.net</span>
      </div>
      <div class="contact">
        <svg viewBox="0 0 24 24" aria-hidden="true"><path d="M6.6 10.8a15 15 0 0 0 6.6 6.6l2.2-2.2a1 1 0 0 1 1-.25 11 11 0 0 0 3.6.6 1 1 0 0 1 1 1V20a1 1 0 0 1-1 1A17 17 0 0 1 3 4a1 1 0 0 1 1-1h3.5a1 1 0 0 1 1 1c0 1.25.2 2.45.6 3.6a1 1 0 0 1-.25 1z"/></svg>
        <span>888-021-447-302-16<br>888-021-447-302-16</span>
      </div>
    </div>

    <h2 class="company">Harbinger<br>Mobile Rig<br>&amp; Machinery Repair</h2>
  </section>
</main>
</body>
</html>
```